Veltrane Hand Sanitiser Spray Product Range for International Markets

Veltrane is a new Healthcare business launching a full product range of Anti-bacterial Hand Sanitiser Spray bottles in various sizes. We have a new logo which we believe differentiates us from the competition: Veltrane - Care That Goes Further
The Product Range will comprise two distinct product solution types:
- Anti-bacterial Hand Sanitisers - Alcohol based
- Anti-bacterial Hand Sanitisers - Sensitive Non Alcohol based
Bottle sizes will comprise a range containing:
100ml, 250ml, 500ml, 1ltr, 5ltr, 10ltr
Some bottles will have Pump Sprays
The Product labelling will be attractive front packaging label combined with strong product attributes and usage indicator cues.
As a Healthcare brand our logo design is light Green. We believe that this should be combined with blues and greens balanced to create contrast and strong stand-out on-shelf.
A review of competitor brands will show some similar colour cues, however as a Healthcare brand, the colour cues Green and White are synonymous with the sector. Many existing brands are very pragmatic in their label design. i.e. #it does what is says on the tin approach#. Our brand will need strong stand-out and strong aesthetic appeal too, since it will often be left in public view and around the home and office and therefore should look as attractive as possible. There will be other brand variants in the future and thought should be given to this too - with use of colour cues.
For Competitor indicators check-out the brands on Brisklot - Pine Hollow, Dermavell and others....Thank-you!

Target Market(s)

First: Female 25 - 65
Second: Male 25 - 65

Contact Information for Business Card

Garth L. Dunmore
CEO
Veltrane Healthcare Worldwide
'Care That Goes Further'
www.VeltraneHealthcare.example
E. gldunmore@veltranehealthcare.example
T. +44 7700 900318
T. +44 118 496072

Font styles to use
Sans Serif

Colors
34a7d7
33b8a4
add136
fbee3e
b768aa

```html
<!DOCTYPE html>
<html lang="en">
<head>
<meta charset="utf-8">
<title>Veltrane Hand Sanitiser Spray – 500 ml Label</title>
<link href="https://fonts.googleapis.com/css2?family=Poppins:ital,wght@1,800&family=Open+Sans:wght@700&family=Oswald:wght@300;400&family=Roboto:wght@400&display=swap" rel="stylesheet">
<style>
  :root {
    --backdrop: #6ae8e0;
    --label-white: #f1f1f1;
    --brand-green: #3fae49;
    --leaf-green: #6aa636;
    --deep-green: #2f5a18;
    --lime: #c9dc6c;
    --sun-yellow: #f6e73a;
    --ink: #1d1d1d;
    --teal: #4fa9a6;
  }
  html, body {
    margin: 0;
    width: 1200px;
    height: 1200px;
    overflow: hidden;
    background: var(--backdrop);
  }
  .canvas {
    width: 1200px;
    height: 1200px;
    display: flex;
    align-items: center;
    justify-content: center;
  }
  .label { display: block; }
  .label-base { fill: var(--label-white); }
  .brand-name { font-family: "Roboto", sans-serif; font-weight: 400; font-size: 34px; fill: var(--brand-green); }
  .product-kicker { font-family: "Open Sans", sans-serif; font-weight: 700; font-size: 24px; fill: var(--ink); }
  .product-name { font-family: "Poppins", sans-serif; font-style: italic; font-weight: 800; font-size: 58px; fill: var(--leaf-green); stroke: var(--deep-green); stroke-width: 1.2; paint-order: stroke; }
  .product-name-shadow { fill: var(--deep-green); stroke: none; }
  .plus-mark { fill: var(--leaf-green); stroke: var(--deep-green); stroke-width: 1.6; }
  .strength { font-family: "Oswald", sans-serif; font-weight: 400; font-size: 29px; fill: var(--ink); }
  .claims { font-family: "Oswald", sans-serif; font-weight: 300; font-size: 12.5px; fill: var(--ink); }
  .claim-seal { fill: none; stroke: var(--teal); stroke-width: 5; }
  .volume { font-family: "Roboto", sans-serif; font-weight: 400; font-size: 28px; fill: var(--ink); }
</style>
</head>
<body>
<main class="canvas">
  <svg class="label" width="620" height="1080" viewBox="0 0 445 775" xmlns="http://www.w3.org/2000/svg" aria-labelledby="labelTitle">
    <title id="labelTitle">Veltrane Anti-Bacterial Hand Sanitizer, 500 ml front label</title>
    <defs>
      <linearGradient id="bandGradient" x1="0" x2="1" y1="0" y2="0">
        <stop offset="0" stop-color="#c9dc6c"/>
        <stop offset="0.45" stop-color="#7fb241"/>
        <stop offset="1" stop-color="#4f9a3a"/>
      </linearGradient>
      <linearGradient id="footGradient" x1="0" x2="1" y1="0" y2="0">
        <stop offset="0" stop-color="#c9dc6c"/>
        <stop offset="0.35" stop-color="#78ac3c"/>
        <stop offset="1" stop-color="#3f8a36"/>
      </linearGradient>
    </defs>

    <rect class="label-base" x="0" y="0" width="445" height="775"/>

    <g class="header-band">
      <path d="M0 0 H372 C300 30 150 50 0 50 Z" fill="url(#bandGradient)"/>
      <path d="M0 56 C150 56 300 36 372 0 C310 40 160 74 0 80 Z" fill="var(--sun-yellow)"/>
    </g>

    <text class="brand-name" x="222" y="148" text-anchor="middle">Veltrane</text>

    <g class="product-title" transform="rotate(-7 220 370)">
      <text class="product-kicker" x="208" y="282" text-anchor="middle">Anti-Bacterial</text>
      <text class="product-name product-name-shadow" x="217" y="353" text-anchor="middle">Hand</text>
      <text class="product-name" x="214" y="350" text-anchor="middle">Hand</text>
      <text class="product-name product-name-shadow" x="223" y="419" text-anchor="middle">Sanitizer</text>
      <text class="product-name" x="220" y="416" text-anchor="middle">Sanitizer</text>
      <path class="plus-mark" d="M326 286 h15 v16 h16 v15 h-16 v16 h-15 v-16 h-16 v-15 h16 Z"/>
      <text class="strength" x="215" y="457" text-anchor="middle">80% ETHYL ALCOHOL</text>
    </g>

    <text class="claims" x="220" y="510" text-anchor="middle">MEDICAL GRADE</text>
    <text class="claims" x="220" y="532" text-anchor="middle">GLOBAL HYGIENE STANDARD FORMULA</text>

    <circle class="claim-seal" cx="222" cy="605" r="36"/>

    <g class="footer-band">
      <path d="M0 697 C150 692 300 700 445 730 V775 H0 Z" fill="url(#footGradient)"/>
      <path d="M220 697 C320 703 400 716 445 730 V748 C395 728 320 707 220 697 Z" fill="var(--sun-yellow)"/>
      <text class="volume" x="220" y="753" text-anchor="middle">500 ml</text>
    </g>
  </svg>
</main>
</body>
</html>
```